Vantor Health Group Presentation Folder, for Cancer Awareness, VERY COLORFUL AND MODERN

Presentation Folder I know pretty much what i want so it should be very eazy , I have included files from folders I use now rebrand them to my new company they will be fine, no sense re creating the wheel
Full Bleed Size
20.87" x 16.68"
53 x 42.4 cm
6260 x 5004 pixels
Document Trim Size
20.75" x 16.56"
52.7 x 42.1 cm
6225 x 4969 pixels
Updates

Low design quality

Industry/Entity Type

Medical

Font styles to use
Serif

Colors

Designer to choose colors to be used in the design.

Requirements
Must have
• really I am not looking for some one to redesign, we like our folder front page and would like to see new word information added., there are two folder front pages to choose from
• So Keep the original front page and redesign the back page and the pockets
• Can Make your Design off of one of the ones I already uploaded
Nice to have
• Keep the same color schemes, Keep the original front page and redesign the back page and the pockets
Should not have
• DO not recreate the front covers, use what I gave you and just rebrand

```html
<!DOCTYPE html>
<html lang="en">
<head>
<meta charset="utf-8">
<title>Vantor Health Group – Hereditary Cancer Screening Folder</title>
<link href="https://fonts.googleapis.com/css2?family=Raleway:wght@300;400;600;700;800&family=Arimo:wght@400;700&display=swap" rel="stylesheet">
<style>
  :root{
    --paper:#ffffff;
    --cut:#e8353b;
    --fold:#3fae6a;
    --pink:#f394a6;
    --pink-photo:#e98aa3;
    --pink-deep:#9c2957;
    --sky:#7fd0f3;
    --blue:#5aabdf;
    --blue-line:#5fa8df;
    --grey-strip:#d1d3d4;
    --ink:#3a3a3a;
    --magenta:#d8168b;
  }
  html,body{margin:0;padding:0;width:1200px;height:960px;overflow:hidden;background:var(--paper);}
  .canvas{position:relative;width:1500px;height:1200px;transform:scale(.8);transform-origin:0 0;}
  .dieline{position:absolute;left:0;top:0;}
  .block{position:absolute;}
  .cover-photo{left:98px;top:77px;width:620px;height:380px;background:linear-gradient(180deg,#f7c9d6 0%,#e98aa3 55%,#b84f75 100%);}
  .quote-box{left:426px;top:384px;width:268px;height:257px;background:var(--blue);box-sizing:border-box;padding:58px 20px 0 26px;
    font-family:'Raleway',sans-serif;font-weight:600;color:#fff;font-size:20.5px;line-height:25px;}
  .intro{left:107px;top:536px;width:276px;font-family:'Arimo',sans-serif;font-size:11px;line-height:15px;color:var(--pink-deep);}
  .intro b{font-weight:700;}
  .texture{left:70px;top:720px;width:670px;height:145px;background:linear-gradient(180deg,rgba(220,220,225,0) 0%,rgba(220,220,225,.35) 100%);}
  .title-band{left:754px;top:78px;width:536px;height:181px;background:var(--sky);}
  .title{left:807px;top:118px;font-family:'Raleway',sans-serif;font-weight:800;font-size:33px;line-height:41px;letter-spacing:4px;color:var(--pink-deep);margin:0;}
  .subtitle{left:807px;top:202px;font-family:'Raleway',sans-serif;font-weight:700;font-size:15px;letter-spacing:1.2px;color:#fff;}
  .ribbon{left:1236px;top:58px;width:64px;height:102px;background:linear-gradient(90deg,#2d6fb5 0%,#f3a9bd 100%);border-radius:30px 30px 6px 6px;}
  .family-photo{left:754px;top:300px;width:690px;height:434px;background:linear-gradient(135deg,#e9edf0 0%,#c9b59a 55%,#8d7458 100%);}
  .caption{left:953px;top:690px;width:491px;height:54px;background:var(--pink);box-sizing:border-box;padding:13px 20px 0 40px;
    font-family:'Arimo',sans-serif;font-weight:700;font-size:12px;line-height:15px;color:var(--pink-deep);}
  .caption-rule{left:993px;top:744px;width:451px;height:7px;background:var(--blue-line);}
  .brand{left:808px;top:784px;display:flex;align-items:center;gap:28px;font-family:'Raleway',sans-serif;color:var(--ink);}
  .brand-mark{width:40px;height:40px;border-radius:50%;background:var(--blue);}
  .brand-name{font-size:15px;font-weight:600;color:var(--ink);}
  .tagline{left:878px;top:794px;font-family:'Raleway',sans-serif;font-size:14.5px;letter-spacing:1.2px;color:var(--ink);}
  .upside{transform:rotate(180deg);transform-origin:center;}
  .partner{left:274px;top:896px;width:264px;text-align:right;font-family:'Raleway',sans-serif;color:var(--magenta);}
  .partner-name{font-size:24px;font-weight:400;letter-spacing:.5px;line-height:28px;}
  .partner-note{font-size:12.5px;color:var(--ink);line-height:16px;}
  .pocket-copy{left:878px;top:996px;width:434px;font-family:'Raleway',sans-serif;font-weight:300;font-size:14px;line-height:19.5px;color:var(--ink);}
</style>
</head>
<body>
<div class="canvas">
  <svg class="dieline" width="1500" height="1200" viewBox="0 0 1500 1200" aria-hidden="true">
    <!-- pockets -->
    <path d="M66 872 H748 L702 1150 Q694 1196 650 1196 H66 Z" fill="var(--pink)" stroke="var(--cut)" stroke-width="1"/>
    <rect x="66" y="872" width="46" height="324" fill="var(--grey-strip)"/>
    <path d="M760 872 H1442 V1196 H852 Q812 1196 804 1150 Z" fill="var(--pink)" stroke="var(--cut)" stroke-width="1"/>
    <rect x="1396" y="872" width="46" height="324" fill="var(--grey-strip)"/>
    <!-- card slits -->
    <g stroke="var(--cut)" stroke-width="1.3">
      <line x1="276" y1="1003" x2="320" y2="958"/>
      <line x1="491" y1="958" x2="536" y2="1003"/>
      <line x1="276" y1="1067" x2="320" y2="1111"/>
      <line x1="491" y1="1111" x2="536" y2="1067"/>
    </g>
    <!-- outer cut line -->
    <path d="M62 872 L8 856 V580 A30 30 0 0 0 8 520 V20 L62 6 H1444 L1492 20 V520 A30 30 0 0 0 1492 580 V856 L1444 872"
          fill="none" stroke="var(--cut)" stroke-width="1"/>
    <!-- folds -->
    <g stroke="var(--fold)" stroke-width="1" stroke-dasharray="3 3" fill="none">
      <line x1="62" y1="6" x2="62" y2="872"/>
      <line x1="753" y1="6" x2="753" y2="872"/>
      <line x1="1444" y1="6" x2="1444" y2="872"/>
      <line x1="62" y1="872" x2="1444" y2="872"/>
    </g>
  </svg>

  <!-- back cover -->
  <div class="block cover-photo" role="img" aria-label="Photo of a multi-generation family holding hands on a seaside shore, pink toned"></div>
  <div class="block quote-box">Don’t be Afraid of the Answer: Knowledge is Power and Power Eradicates Fear. When You are Fear-less, You Will Make all the Right Choices!</div>
  <p class="block intro" style="margin:0"><b>Hereditary cancer screening</b> provides vital information to help people with a strong personal or family history of cancer understand their own risk of developing the disease. With this information, they can take steps to Potentially Prevent Cancer, Delay the Onset of Cancer or Catch it at an Earlier stage when outcomes and survival rates are Better.</p>
  <div class="block texture" role="img" aria-label="Faint scattered diamond texture"></div>

  <!-- front cover -->
  <div class="block title-band"></div>
  <h1 class="block title">HEREDITARY<br>CANCER SCREENING</h1>
  <div class="block subtitle">Doctors are the Gatekeepers to Genetic Testing</div>
  <div class="block ribbon" role="img" aria-label="Blue and pink awareness ribbon"></div>
  <div class="block family-photo" role="img" aria-label="Photo of a family sharing a meal at an outdoor table"></div>
  <div class="block caption">We have an obligation to help patients understand genetic risk and how testing can guide heath care decisions.</div>
  <div class="block caption-rule"></div>
  <div class="block brand" style="top:781px"><span class="brand-mark"></span></div>
  <div class="block tagline">The test you order FOR your patients</div>

  <!-- pockets copy -->
  <div class="block partner upside">
    <div class="partner-name">Arden Wealth Partners</div>
    <div class="partner-note">an independent arm of Corvell Labs LLC</div>
  </div>
  <p class="block pocket-copy upside" style="margin:0">At our state of the art, CLIA certified and COLA accredited facility we perform Next Generation Sequencing (NGS) based screening for mutations known to affect an individual's Risk of developing Hereditary Cancer. Results from the test enable the Physician to make better informed treatment decisions.</p>
</div>
</body>
</html>
```